Harborline Finish Works business cards

we sandblast, power tool, and paint Navy ships and steel structures. When we paint we use brushes, rollers, and airless sprayers. We do marine work as well as industrial. Some things that are important for our customer to know is Quality, Safety, Excellence, Dependability and Professional. We definitely would like to have our company logo that was designed here on art kiosk incorporated into the business card. We are open for suggestions as far as the design goes.

Target Market(s)

marine and industrial

Industry/Entity Type

Painting

Contact Information for Business Card

Derek Mallow
612-385-2049
dmallow@hlfworks.example

Font styles to use
Serif
Decorative
Script

Colors
fbed22
000000
ffffff

Requirements
Must have
• company logo that is uploaded

```html
<!DOCTYPE html>
<html lang="en">
<head>
<meta charset="utf-8">
<title>Harborline Finish Works – Business Cards</title>
<link rel="stylesheet" href="https://fonts.googleapis.com/css2?family=Cinzel:wght@400;700&family=Lato:wght@400&display=swap">
<style>
  :root {
    --backdrop: #d6d6d4;
    --card-black: #0a0a0a;
    --gold: #d9a938;
    --gold-bright: #fbed22;
    --white: #ffffff;
  }
  * { margin: 0; padding: 0; box-sizing: border-box; }
  html, body {
    width: 1200px;
    height: 999px;
    overflow: hidden;
    background: var(--backdrop);
  }
  .sheet {
    position: relative;
    width: 1200px;
    height: 999px;
  }
  .card {
    position: absolute;
    left: 230px;
    width: 740px;
    height: 423px;
    background: var(--card-black);
    box-shadow: 0 6px 18px rgba(0,0,0,0.25);
    overflow: hidden;
  }
  .card--back { top: 50px; }
  .card--front { top: 526px; }

  .rule {
    position: absolute;
    left: 40px;
    right: 40px;
    height: 2px;
    background: linear-gradient(90deg, rgba(217,169,56,0) 0%, var(--gold) 20%, var(--gold-bright) 50%, var(--gold) 80%, rgba(217,169,56,0) 100%);
  }
  .card--back .rule--top { top: 44px; }
  .card--back .rule--bottom { bottom: 58px; }
  .card--front .rule--divider { top: 200px; left: 60px; right: 60px; }

  .brand {
    position: absolute;
    left: 0;
    right: 0;
    text-align: center;
    color: var(--gold);
    font-family: "Cinzel", serif;
    font-weight: 700;
  }
  .brand__mark {
    display: block;
    margin: 0 auto;
    border-radius: 50%;
    border: 3px solid var(--gold);
  }
  .card--back .brand { top: 112px; }
  .card--back .brand__mark { width: 74px; height: 74px; margin-bottom: 22px; }
  .card--back .brand__name { font-size: 40px; letter-spacing: 1px; line-height: 1.1; }

  .card--front .brand { top: 62px; }
  .card--front .brand__mark { width: 50px; height: 50px; margin-bottom: 14px; }
  .card--front .brand__name { font-size: 28px; letter-spacing: 1px; line-height: 1.1; }

  .holder {
    position: absolute;
    top: 226px;
    left: 0;
    right: 0;
    text-align: center;
    font-family: "Cinzel", serif;
    font-weight: 400;
    font-size: 42px;
    color: var(--gold);
    letter-spacing: 1px;
  }
  .contact {
    position: absolute;
    top: 300px;
    left: 236px;
    list-style: none;
    font-family: "Lato", sans-serif;
    font-size: 21px;
    color: var(--gold);
  }
  .contact__item {
    display: flex;
    align-items: center;
    gap: 10px;
    height: 32px;
  }
  .contact__icon {
    width: 18px;
    height: 18px;
    flex: none;
  }
</style>
</head>
<body>
<main class="sheet">

  <section class="card card--back" aria-label="Business card back">
    <div class="rule rule--top"></div>
    <div class="brand">
      <span class="brand__mark"></span>
      <span class="brand__name">HARBORLINE FINISH WORKS</span>
    </div>
    <div class="rule rule--bottom"></div>
  </section>

  <section class="card card--front" aria-label="Business card front">
    <div class="brand">
      <span class="brand__mark"></span>
      <span class="brand__name">HARBORLINE FINISH WORKS</span>
    </div>
    <div class="rule rule--divider"></div>
    <h1 class="holder">DEREK MALLOW</h1>
    <ul class="contact">
      <li class="contact__item">
        <svg class="contact__icon" viewBox="0 0 18 18" aria-hidden="true">
          <rect x="5" y="1" width="8" height="16" rx="1.5" fill="none" stroke="#d9a938" stroke-width="1.6"/>
          <circle cx="9" cy="14" r="1" fill="#d9a938"/>
        </svg>
        <span>612-385-2049</span>
      </li>
      <li class="contact__item">
        <svg class="contact__icon" viewBox="0 0 18 18" aria-hidden="true">
          <rect x="1" y="4" width="16" height="11" rx="1" fill="#d9a938"/>
          <path d="M1.5 4.5 L9 10 L16.5 4.5" fill="none" stroke="#0a0a0a" stroke-width="1.4"/>
        </svg>
        <span>dmallow@hlfworks.example</span>
      </li>
    </ul>
  </section>

</main>
</body>
</html>
```